Boutique Financial Services/Advisor Business Needs Web Design

Looking for an informational and functional web design for my Financial Services/Financial Advisement business. It should have functionality for Company name, address, phone #, "About Us", Who we are, Our Mission, Services we offer, Biographies/Photos of/about "The Team", and possibly a link to "Contact Us". Would like to see something new & exciting blended with a traditional/professional look that will appeal to those approaching retirement, as well as those younger clients that are beginning to think about planning for the future. I already have a web domain through HostMeadow, but would like this to be the design we use for that domain.
Financial Services/Financial Advisor
Coded - Design and coding required
1 page

```html
<!DOCTYPE html>
<html lang="en">
<head>
<meta charset="utf-8">
<title>Summitline Wealth Partners</title>
<link rel="stylesheet" href="https://fonts.googleapis.com/css2?family=Josefin+Sans:wght@400;500;600;700&display=swap">
<style>
:root{
  --navy:#0b2e78;
  --royal:#0a55b5;
  --royal-dark:#0a4aa6;
  --sky:#5aa6ec;
  --tile:#2e62c0;
  --deep:#0a2a66;
  --ink:#1e2a44;
  --heading:#0c3a8c;
  --muted:#3b4152;
  --panel:#e9eef6;
  --footer:#232528;
  --white:#ffffff;
}
*{box-sizing:border-box;margin:0;padding:0}
html,body{width:1200px;height:3228px;overflow:hidden}
body{position:relative;font-family:"Josefin Sans",sans-serif;color:var(--ink);background:var(--white)}
.abs{position:absolute}
.center{text-align:center}

/* header */
.site-header{left:0;top:0;width:1200px;height:110px;background:var(--navy)}
.btn-pill{display:block;border-radius:20px;font-weight:500;text-align:center}
.header-contact{left:63px;top:38px;width:127px;height:34px;line-height:36px;background:var(--sky);color:var(--white);font-size:14px}
.header-social{left:231px;top:45px;display:flex;gap:13px}
.dot{width:20px;height:20px;border-radius:50%;background:var(--white)}
.brand-mark{left:450px;top:34px;width:300px;color:var(--white);font-weight:600;font-size:19px;letter-spacing:1px;line-height:22px;text-align:center}
.main-nav{left:784px;top:0;display:flex;height:110px}
.main-nav a{color:var(--white);text-decoration:none;font-size:15px;padding:48px 13px 0;height:110px}
.main-nav a.active{background:var(--sky);padding:46px 6px 0}

/* hero */
.hero{left:0;top:110px;width:1200px;height:426px;background:radial-gradient(ellipse at 60% 45%,#1d4fa0 0%,#0c2a66 35%,#061634 70%,#040c1e 100%)}
.hero-title{left:0;top:236px;width:1200px;font-size:45px;font-weight:700;color:var(--white)}
.hero-sub{left:225px;top:306px;width:750px;font-size:14px;line-height:15px;color:var(--white)}
.hero-cta{left:506px;top:354px;width:199px;height:32px;line-height:34px;background:var(--white);color:var(--navy);font-size:14px}

.feature{top:490px;width:318px;height:95px;background:linear-gradient(120deg,#2c5fc0,#3a70cf);display:flex;align-items:center;padding-left:48px;gap:18px;color:var(--white);font-size:19px;font-weight:500}
.feature-icon{width:55px;height:55px;border-radius:50%;background:var(--white);display:flex;align-items:center;justify-content:center;flex:none}

/* who we are */
.who-photo{left:63px;top:648px;width:537px;height:407px;background:linear-gradient(135deg,#e6e9ee,#b9c0ca 55%,#6d6f78)}
.who-panel{left:600px;top:648px;width:537px;height:407px;background:var(--royal)}
.who-title{left:622px;top:733px;font-size:45px;font-weight:700;color:var(--white)}
.who-text{left:622px;top:804px;width:496px;font-size:13.5px;line-height:14.4px;color:var(--white)}
.who-cta{left:621px;top:928px;width:164px;height:33px;line-height:35px;background:var(--sky);color:var(--white);font-size:14px}

/* offer */
.section-title{left:0;width:1200px;font-size:45px;font-weight:700;color:var(--heading);text-align:center}
.section-desc{left:175px;width:850px;font-size:13px;line-height:14.5px;color:var(--muted);text-align:center}
.offer-card{top:1236px;width:250px;height:312px;overflow:hidden}
.offer-image{width:250px;height:268px}
.offer-label{width:250px;height:44px;line-height:48px;background:var(--royal);color:var(--white);text-align:center;font-size:18px;font-weight:500}
.offer-featured{background:linear-gradient(160deg,#1a5bc4,#0a4aa6);color:var(--white);text-align:center;padding-top:64px}
.offer-featured .badge{width:78px;height:78px;border-radius:50%;background:var(--white);margin:0 auto 14px;display:flex;align-items:center;justify-content:center;box-shadow:0 0 0 5px rgba(255,255,255,.35)}
.offer-featured h3{font-size:19px;font-weight:500;margin-bottom:6px}
.offer-featured p{font-size:13px;line-height:14px;padding:0 30px}
.offer-featured a{display:inline-block;margin-top:10px;color:var(--white);font-size:13px;text-decoration:underline}
.pager{left:570px;top:1574px;display:flex;gap:8px}
.pager span{width:11px;height:11px;border:1.5px solid var(--royal);transform:rotate(45deg)}
.pager span.on{background:var(--royal)}

/* contact */
.contact-band{left:0;top:1652px;width:1200px;height:524px;background:radial-gradient(ellipse at 70% 40%,#1f5cbd,#0b2f78 60%,#08225a)}
.contact-form{left:134px;top:1708px;width:526px;height:406px;background:var(--royal-dark)}
.contact-info{left:660px;top:1708px;width:406px;height:406px;background:linear-gradient(135deg,#f2f5fa,#dde5f1)}
.contact-heading{font-size:44px;font-weight:700}
.field{position:absolute;background:var(--white);border:none;font-family:inherit;font-size:13px;color:#5a6070;padding:4px 14px 0;height:29px}
.field-area{height:80px;padding-top:10px;line-height:14px;resize:none}
.form-submit{left:175px;top:2027px;width:141px;height:32px;line-height:34px;background:var(--sky);color:var(--white);font-size:14px}
.info-row{left:700px;display:flex;gap:14px;align-items:flex-start;font-size:18px;color:var(--ink);font-weight:500;line-height:19px}
.info-icon{width:32px;height:32px;border-radius:50%;background:var(--royal);display:flex;align-items:center;justify-content:center;flex:none}

/* team */
.team-arrows{left:1079px;top:2306px;display:flex;gap:7px}
.team-arrows span{width:25px;height:25px;background:var(--royal);display:flex;align-items:center;justify-content:center}
.member{top:2356px;width:230px;text-align:center}
.member-ring{width:228px;height:228px;border-radius:50%;border:2px dashed var(--royal);position:relative}
.member-photo{position:absolute;left:6px;top:6px;width:212px;height:212px;border-radius:50%;background:radial-gradient(circle at 50% 35%,#e7e9ee,#b7bdc8 60%,#5a6274)}
.member h4{font-size:19px;font-weight:500;margin-top:20px;color:var(--ink)}
.member p{font-size:14px;color:var(--muted);margin-top:8px}
.member-social{display:flex;gap:14px;justify-content:center;margin-top:14px}
.member-social span{width:24px;height:24px;border-radius:50%;background:var(--royal)}

/* newsletter */
.newsletter{left:0;top:2733px;width:1200px;height:157px;background:var(--royal)}
.news-title{left:63px;top:2757px;font-size:45px;font-weight:700;color:var(--white)}
.news-text{left:63px;top:2831px;width:560px;font-size:13px;line-height:14.5px;color:var(--white)}
.news-form{left:753px;top:2795px;width:385px;height:32px;border-radius:16px;background:var(--white);overflow:hidden}
.news-form .placeholder{position:absolute;left:14px;top:10px;font-size:13px;color:#5a6070}
.news-form .go{position:absolute;right:0;top:0;width:126px;height:32px;line-height:34px;border-radius:16px;background:var(--sky);color:var(--white);text-align:center;font-size:14px}

/* footer */
.site-footer{left:0;top:2890px;width:1200px;height:338px;background:var(--footer)}
.foot-col{top:2942px;color:var(--white)}
.foot-col h5{font-size:18px;font-weight:500;color:var(--sky);margin-bottom:18px}
.foot-col ul{color:var(--white)}
.foot-col li{list-style:none;font-size:14px;height:33px;color:var(--white)}
.follow li{display:flex;align-items:center;gap:10px;height:37px;font-size:15px}
.follow li span{width:20px;height:20px;border-radius:50%;background:var(--white)}
.foot-brand{left:440px;top:3012px;width:280px;font-size:21px;font-weight:600;letter-spacing:1px;line-height:24px;text-align:center;color:var(--white)}
.foot-rule{left:0;top:3166px;width:1200px;height:1px;background:#4a4d52}
.copyright{left:0;top:3190px;width:1200px;text-align:center;font-size:13px;color:var(--white)}
</style>
</head>
<body>

<header class="abs site-header"></header>
<a class="abs btn-pill header-contact">Contact Us</a>
<div class="abs header-social"><span class="dot"></span><span class="dot"></span><span class="dot"></span><span class="dot"></span></div>
<div class="abs brand-mark">SUMMITLINE WEALTH<br>PARTNERS</div>
<nav class="abs main-nav"><a class="active">Home</a><a>About Us</a><a>Our Services</a><a>Our Team</a></nav>

<section class="abs hero" role="img" aria-label="Hand touching a glowing rising arrow over a growth bar chart"></section>
<h1 class="abs hero-title center">Smart Solutions for Financial Growth</h1>
<p class="abs hero-sub center">We hope your visit will help you understand the opportunities and potential rewards that are available when you take a proactive approach to your personal financial situation.</p>
<a class="abs btn-pill hero-cta">Get Started Today</a>

<div class="abs feature" style="left:63px"><span class="feature-icon"><svg width="28" height="28" viewBox="0 0 28 28"><path d="M6 14l6 6 10-12" fill="none" stroke="#0a55b5" stroke-width="3" stroke-linecap="round"/></svg></span>Trusted Company</div>
<div class="abs feature" style="left:441px"><span class="feature-icon"><svg width="30" height="30" viewBox="0 0 30 30"><circle cx="15" cy="15" r="12" fill="none" stroke="#0a55b5" stroke-width="2.5"/><circle cx="15" cy="15" r="7" fill="none" stroke="#0a55b5" stroke-width="2.5"/><circle cx="15" cy="15" r="2.5" fill="#0a55b5"/></svg></span>Always Plan Flexibly</div>
<div class="abs feature" style="left:819px"><span class="feature-icon"><svg width="30" height="28" viewBox="0 0 30 28"><path d="M3 4h18v12H10l-5 4v-4H3z" fill="none" stroke="#0a55b5" stroke-width="2.2" stroke-linejoin="round"/><path d="M24 9h3v11h-2v4l-4-4h-8" fill="none" stroke="#0a55b5" stroke-width="2.2" stroke-linejoin="round"/></svg></span>24/7 Fast Support</div>

<div class="abs who-photo" role="img" aria-label="Advisor presenting at a whiteboard to a small team in a bright office"></div>
<div class="abs who-panel"></div>
<h2 class="abs who-title">Who We Are</h2>
<p class="abs who-text">We hope your visit will help you understand the opportunities and potential rewards that are available when you take a proactive approach to your personal financial situation. We have created this Web site to help you gain a better understanding of the financial concepts behind insurance, investing, retirement, estate planning, and wealth preservation. Most important, we hope you see the value of working with skilled professionals to pursue your financial goals.</p>
<a class="abs btn-pill who-cta">Find Out More</a>

<h2 class="abs section-title" style="top:1110px">What We Offer</h2>
<p class="abs section-desc" style="top:1183px">We are a full-service financial practice committed to helping people pursue their financial goals. We offer a wide range of financial products and services to individuals and business owners. We believ</p>

<article class="abs offer-card offer-featured" style="left:63px">
  <div class="badge"><svg width="40" height="36" viewBox="0 0 40 36"><path d="M4 16L20 4l16 12" fill="none" stroke="#0a55b5" stroke-width="2.5"/><rect x="9" y="15" width="22" height="17" fill="none" stroke="#0a55b5" stroke-width="2.5"/><rect x="17" y="22" width="6" height="10" fill="#0a55b5"/></svg></div>
  <h3>Estate Planning</h3>
  <p>Lorem ipsum odor amet, consectetuer adipiscing elit. Cubilia efficitur</p>
  <a>Read More</a>
</article>
<article class="abs offer-card" style="left:337px"><div class="offer-image" role="img" aria-label="Hand touching a glowing tax icon display" style="background:radial-gradient(circle at 50% 50%,#3b8fb0,#0f3f5c 60%,#082637)"></div><div class="offer-label">Tax Planning</div></article>
<article class="abs offer-card" style="left:612px"><div class="offer-image" role="img" aria-label="Stacks of coins before a city skyline with market figures" style="background:linear-gradient(180deg,#2a3f66,#3c5a86 55%,#b08a3e)"></div><div class="offer-label">Wealth Management</div></article>
<article class="abs offer-card" style="left:888px"><div class="offer-image" role="img" aria-label="Hands with a phone and laptop beneath rising year markers" style="background:linear-gradient(135deg,#c9ccd0,#8c8f94 55%,#3e4a3a)"></div><div class="offer-label">Financial Planning</div></article>
<div class="abs pager"><span class="on"></span><span></span><span></span></div>

<section class="abs contact-band" role="img" aria-label="Blue background with a faint rising arrow and year graphic"></section>
<div class="abs contact-form"></div>
<div class="abs contact-info"></div>
<h2 class="abs contact-heading" style="left:175px;top:1764px;color:var(--white)">Contact Our Team</h2>
<input class="field" style="left:175px;top:1834px;width:442px" placeholder="Name">
<input class="field" style="left:175px;top:1879px;width:213px" placeholder="E-Mail">
<input class="field" style="left:401px;top:1879px;width:216px" placeholder="Phone Number">
<textarea class="field field-area" style="left:175px;top:1924px;width:442px" placeholder="How Can We Help You ?"></textarea>
<a class="abs btn-pill form-submit">Submit</a>
<h2 class="abs contact-heading" style="left:703px;top:1792px;color:var(--heading)">Contact Us</h2>
<div class="abs info-row" style="top:1862px"><span class="info-icon"><svg width="16" height="12" viewBox="0 0 16 12"><rect x="1" y="1" width="14" height="10" rx="1" fill="none" stroke="#fff" stroke-width="1.6"/><path d="M1 2l7 5 7-5" fill="none" stroke="#fff" stroke-width="1.6"/></svg></span><span style="padding-top:8px">info@summitlinewealth.com</span></div>
<div class="abs info-row" style="top:1926px"><span class="info-icon"><svg width="16" height="16" viewBox="0 0 16 16"><path d="M3 1l3 3-2 2c1 2 3 4 5 5l2-2 3 3-2 3C7 15 1 9 1 3z" fill="none" stroke="#fff" stroke-width="1.5" stroke-linejoin="round"/></svg></span><span style="padding-top:8px">555-014-2290</span></div>
<div class="abs info-row" style="top:1992px"><span class="info-icon"><svg width="14" height="18" viewBox="0 0 14 18"><path d="M7 17S1 10 1 6.5a6 6 0 0112 0C13 10 7 17 7 17z" fill="none" stroke="#fff" stroke-width="1.6"/><circle cx="7" cy="6.5" r="2" fill="#fff"/></svg></span><span style="padding-top:2px">1840 Harlow Avenue, Suite<br>210 Brookfield, OH</span></div>

<h2 class="abs section-title" style="top:2232px">Get To Know Our Team</h2>
<p class="abs section-desc" style="top:2304px">We are a full-service financial practice committed to helping people pursue their financial goals. We offer a wide range of financial products and services to individuals and business owners. We believ</p>
<div class="abs team-arrows"><span><svg width="8" height="12"><path d="M7 1L2 6l5 5" fill="none" stroke="#fff" stroke-width="2"/></svg></span><span><svg width="8" height="12"><path d="M1 1l5 5-5 5" fill="none" stroke="#fff" stroke-width="2"/></svg></span></div>

<div class="abs member" style="left:60px"><div class="member-ring"><div class="member-photo" role="img" aria-label="Portrait of a senior man in a navy suit"></div></div><h4>Henry</h4><p>Head of Human Resources</p><div class="member-social"><span></span><span></span><span></span></div></div>
<div class="abs member" style="left:343px"><div class="member-ring"><div class="member-photo" role="img" aria-label="Portrait of a woman in a blue blazer"></div></div><h4>Lily</h4><p>Non-Executive Director</p><div class="member-social"><span></span><span></span><span></span></div></div>
<div class="abs member" style="left:627px"><div class="member-ring"><div class="member-photo" role="img" aria-label="Portrait of a man in a suit and tie"></div></div><h4>John</h4><p>Chief Operating</p><div class="member-social"><span></span><span></span><span></span></div></div>
<div class="abs member" style="left:910px"><div class="member-ring"><div class="member-photo" role="img" aria-label="Portrait of a woman in a black suit"></div></div><h4 style="font-size:16px;margin-top:18px">Luna</h4><p style="font-size:13px">Managing Director</p><div class="member-social"><span></span><span></span><span></span></div></div>

<section class="abs newsletter"></section>
<h2 class="abs news-title">Subscribe To Our News Letter</h2>
<p class="abs news-text">Lorem ipsum odor amet, consectetuer adipiscing elit. Cubilia efficitur cras integer sollicitudin enim aliquam. Aptent felis alique.</p>
<div class="abs news-form"><span class="placeholder">Enter Email Address</span><span class="go">Submit</span></div>

<footer class="abs site-footer"></footer>
<div class="abs foot-col" style="left:63px"><h5>Navigation</h5><ul><li>Home</li><li>About Us</li><li>Our Services</li><li>Our Team</li></ul></div>
<div class="abs foot-col" style="left:251px"><h5>Quick Link</h5><ul><li>FAQ</li><li>News Letters</li><li>Privacy Policy</li><li>Term &amp; Conditions</li></ul></div>
<div class="abs foot-brand">SUMMITLINE WEALTH<br>PARTNERS</div>
<div class="abs foot-col" style="left:787px"><h5 style="padding-left:6px">Our services</h5><ul><li>Estate Planning</li><li>Tax Planning</li><li>Financial Planning</li><li>Retirement Planning</li></ul></div>
<div class="abs foot-col follow" style="left:1032px"><h5>Follow Us</h5><ul><li><span></span>Circlebook</li><li><span></span>Pictogram</li><li><span></span>Chirper</li><li><span></span>Linkwork</li></ul></div>
<div class="abs foot-rule"></div>
<p class="abs copyright">© 2024 All Rights Reserved</p>

</body>
</html>
```